Letterhead for small civil engineer company

We need bold and modern design for company letterhead in MS word. It needs to have company logo and company info. Somewhere in the upper right part of document needs to be space for "recever" and the documents starts with, example, "SUBJECT: CIVIL ENGINEER LETTERHEAD".

in the bottom part of document needs to be signature and date.

Company info: Veltrana d.o.o., Lipovac 15, Lipovac (Općina Brdarić), OIB 47396028154, www.veltrana.hr, info@veltrana.hr

Email of document sender needs to be somewhere if document, exapmle xyz@veltrana.hr

Target Market(s)

Civil engineer company and projects

Industry/Entity Type

Civil engineer

Font styles to use
Serif

Colors
F0912C
F2A743
F7CA91
FBE8D2
FDF5EE

Requirements
Must have
• Company logo and company info
Nice to have
• Moder and clean design
Should not have
• Too much details

```html
<!DOCTYPE html>
<html lang="hr">
<head>
<meta charset="utf-8">
<title>Veltrana d.o.o. – Letterhead</title>
<link rel="stylesheet" href="https://fonts.googleapis.com/css2?family=Tinos:wght@400;700&family=Great+Vibes&display=swap">
<style>
  :root {
    --orange: #F0912C;
    --orange-mid: #F2A743;
    --peach: #F7CA91;
    --cream: #FBE8D2;
    --paper: #FDFDFB;
    --ink: #3a3a3a;
    --rule: #b9b9b9;
    --info-red: #e2574c;
    --backdrop: #1c1c1e;
  }
  * { box-sizing: border-box; margin: 0; padding: 0; }
  html, body { width: 1200px; height: 1000px; overflow: hidden; background: var(--backdrop); }
  body { font-family: "Tinos", "Times New Roman", serif; color: var(--ink); }

  .letterhead {
    position: absolute; left: 275px; top: 40px;
    width: 650px; height: 920px;
    background: var(--paper);
    overflow: hidden;
  }

  .brand { position: absolute; left: 58px; top: 52px; display: flex; align-items: center; gap: 10px; }
  .brand-mark { width: 20px; height: 20px; border: 2px solid var(--orange); }
  .brand-name { font-size: 24px; font-weight: 700; letter-spacing: 2px; color: var(--orange); }
  .brand-underline { position: absolute; left: 58px; top: 90px; width: 120px; height: 3px; background: var(--orange); }

  .header-rule { position: absolute; left: 190px; top: 118px; right: 0; height: 1px; background: var(--rule); }

  .company-info { position: absolute; left: 58px; top: 104px; font-size: 12.5px; line-height: 17px; }
  .company-info .label { color: var(--info-red); }

  .subject { position: absolute; left: 58px; top: 210px; font-size: 13px; font-weight: 700; letter-spacing: .2px; }

  .receiver { position: absolute; right: 40px; top: 300px; width: 230px; }
  .receiver .label { display: block; text-align: right; font-size: 12px; margin-bottom: 22px; }
  .receiver .line { height: 1px; background: var(--rule); }

  .signature { position: absolute; left: 58px; top: 650px; }
  .signature .name { font-family: "Great Vibes", cursive; font-size: 30px; color: #555; }
  .signature .label { font-size: 11px; margin-top: -4px; }

  .footer-art {
    position: absolute; left: 0; right: 0; bottom: 18px; height: 200px;
    background: linear-gradient(180deg, rgba(235,235,232,0) 0%, #ececea 100%);
  }
  .footer-accent { position: absolute; left: 58px; top: 722px; width: 110px; height: 3px; background: var(--orange); }

  .contact { position: absolute; left: 58px; top: 800px; display: flex; align-items: center; gap: 10px; font-size: 12px; line-height: 15px; }
  .contact svg { width: 24px; height: 18px; }

  .date { position: absolute; right: 40px; top: 790px; width: 230px; }
  .date .label { display: block; font-size: 12px; margin-bottom: 22px; }
  .date .line { height: 1px; background: var(--rule); }

  .bottom-band { position: absolute; left: 0; right: 0; bottom: 0; height: 18px; background: linear-gradient(90deg, var(--orange), var(--orange-mid)); }
</style>
</head>
<body>
  <main class="letterhead">
    <div class="brand">
      <span class="brand-mark"></span>
      <span class="brand-name">VELTRANA</span>
    </div>
    <div class="brand-underline"></div>
    <div class="header-rule"></div>

    <address class="company-info" style="font-style:normal">
      <span class="label">Company info:</span><br>
      Veltrana d.o.o., Lipovac 15,<br>
      Lipovac (Općina Brdarić),<br>
      OIB 47396028154
    </address>

    <p class="subject">SUBJECT: CIVIL ENGINEER LETTERHEAD</p>

    <div class="receiver">
      <span class="label">Receiver:</span>
      <div class="line"></div>
    </div>

    <div class="signature">
      <div class="name">Ivan Perić</div>
      <div class="label">signature</div>
    </div>

    <div class="footer-art" role="img" aria-label="Faint architectural line drawing of a building along the page foot"></div>
    <div class="footer-accent"></div>

    <div class="contact">
      <svg viewBox="0 0 24 18" aria-hidden="true">
        <rect x="1" y="1" width="22" height="16" fill="none" stroke="var(--orange)" stroke-width="1.6"/>
        <polyline points="1,1 12,10 23,1" fill="none" stroke="var(--orange)" stroke-width="1.6"/>
      </svg>
      <div>www.veltrana.hr<br>info@veltrana.hr</div>
    </div>

    <div class="date">
      <span class="label">Date:</span>
      <div class="line"></div>
    </div>

    <div class="bottom-band"></div>
  </main>
</body>
</html>
```